We are a specialised Chartered Accountant recruiting business and we are hosting a Casino Night for newly qualified CAs.1. We need a flyer Designed that will be sent out to all newly qualified CAs with 1. Information about the event and to 2. probe them to attendThe below information to be included:Date : 07th of November 2019 (Thursday)Venue : Velvet Lantern Tavern Johannesburg | Orwin Tembe Plaza, 14 Corvell Lane, SandtonArrive : 18: 30 Dress code : Smart Casual / CocktailEntertainment : Drinks & Snacks will be provided RSVP : Pelovin Representative
Target Market(s)
23 - 27 year olds
Colors
Designer to choose colors to be used in the design.
Requirements
Must have
- The Flyer must have the event Title " Amber Staffing Pelovin Casino Night
- Must have the below details
- Date : 07th of November 2019 (Thursday)
- Venue : Velvet Lantern Tavern Johannesburg | Orwin Tembe Plaza, 14 Corvell Lane,
- Sandton
- Arrive : 18: 30
- Dress code : Smart Casual / Cocktail
- Entertainment : Drinks & Snacks will be provided
- RSVP : Pelovin Representative
Nice to have
- Can use either one of the images we sent through not necessarily both
Should not have
- Must have all the details i have provided about the event.
- Must have a catchy line inviting people to come to the event.

```html
<!DOCTYPE html>
<html lang="en">
<head>
<meta charset="utf-8">
<title>Amber Staffing Pelovin Casino Night</title>
<link rel="stylesheet" href="https://fonts.googleapis.com/css2?family=Oswald:wght@500;600&family=Open+Sans:wght@400;600&family=Great+Vibes&display=swap">
<style>
  :root {
    --ink: #0b0b0c;
    --gold: #e9b233;
    --gold-deep: #b8861c;
    --gold-pale: #f7dc85;
    --silver-light: #ffffff;
    --silver-mid: #b9bbbf;
    --text: #f2f2f2;
    --accent: #f0a930;
  }
  * { margin: 0; padding: 0; box-sizing: border-box; }
  html, body { width: 993px; height: 1200px; overflow: hidden; background: var(--ink); }
  .flyer {
    position: relative;
    width: 993px;
    height: 1200px;
    overflow: hidden;
    background: radial-gradient(ellipse at 50% 75%, #1e1e20 0%, var(--ink) 70%);
    font-family: "Open Sans", Arial, sans-serif;
    color: var(--text);
  }
  .hero-photo {
    position: absolute;
    left: 0; top: 0;
    width: 993px; height: 600px;
    background:
      radial-gradient(ellipse at 50% 40%, rgba(230,225,220,0.55) 0%, rgba(120,110,100,0) 45%),
      radial-gradient(ellipse at 30% 30%, #8a6a4a 0%, rgba(60,40,30,0) 40%),
      radial-gradient(ellipse at 75% 30%, #6b4a30 0%, rgba(60,40,30,0) 40%),
      linear-gradient(180deg, #3a2a1c 0%, #2a2220 55%, #0b0b0c 100%);
  }
  .hero-band {
    position: absolute;
    left: 0; top: 540px;
    width: 993px; height: 110px;
    background: linear-gradient(180deg, rgba(11,11,12,0) 0%, #000 40%, #000 100%);
  }
  .frame-art {
    position: absolute;
    inset: 0;
    width: 993px; height: 1200px;
  }
  .content {
    position: absolute;
    left: 0; right: 0; top: 445px;
    text-align: center;
  }
  .event-host {
    font-family: "Oswald", Arial, sans-serif;
    font-weight: 600;
    font-size: 40px;
    line-height: 1.3;
    letter-spacing: 0.5px;
    text-transform: uppercase;
    color: var(--text);
    text-shadow: 0 2px 6px rgba(0,0,0,0.8);
  }
  .event-title {
    font-family: "Oswald", Arial, sans-serif;
    font-weight: 500;
    font-size: 140px;
    line-height: 1;
    letter-spacing: 4px;
    text-transform: uppercase;
    background: linear-gradient(180deg, var(--silver-light) 0%, #e6e7ea 45%, var(--silver-mid) 55%, #eeeeef 100%);
    -webkit-background-clip: text;
    background-clip: text;
    color: transparent;
  }
  .event-script {
    font-family: "Great Vibes", cursive;
    font-size: 88px;
    line-height: 0.8;
    color: var(--text);
    margin-top: -22px;
  }
  .event-date {
    font-family: "Oswald", Arial, sans-serif;
    font-weight: 500;
    font-size: 32px;
    line-height: 1.35;
    color: var(--accent);
    margin-top: 24px;
  }
  .divider {
    width: 500px;
    height: 2px;
    margin: 11px auto;
    background: linear-gradient(90deg, rgba(233,178,51,0.2), var(--gold-pale), rgba(233,178,51,0.2));
  }
  .venue {
    font-size: 20px;
    line-height: 1.4;
    color: var(--text);
  }
  .extras {
    font-size: 20px;
    line-height: 1.3;
    color: var(--accent);
  }
  .invite-line {
    font-family: "Great Vibes", cursive;
    font-size: 30px;
    line-height: 1.1;
    color: var(--text);
    margin-top: 8px;
  }
  .rsvp {
    display: inline-block;
    margin-top: 14px;
    padding: 8px 34px;
    border-radius: 16px;
    background: linear-gradient(90deg, var(--gold-deep) 0%, var(--gold-pale) 35%, var(--gold) 65%, #fff3c4 100%);
    font-family: "Oswald", Arial, sans-serif;
    font-weight: 500;
    font-size: 23px;
    line-height: 1.3;
    color: #1a1208;
    text-transform: uppercase;
    letter-spacing: 0.5px;
  }
</style>
</head>
<body>
  <main class="flyer">
    <div class="hero-photo" role="img" aria-label="Photo of four smiling guests at a casino with playing cards, poker chips and dice in front"></div>
    <div class="hero-band"></div>

    <svg class="frame-art" viewBox="0 0 993 1200" aria-hidden="true">
      <defs>
        <linearGradient id="gold-line" x1="0" y1="0" x2="1" y2="1">
          <stop offset="0" stop-color="#b8861c"/>
          <stop offset="0.45" stop-color="#f7dc85"/>
          <stop offset="1" stop-color="#d39a24"/>
        </linearGradient>
      </defs>
      <g fill="none" stroke="url(#gold-line)">
        <rect x="80" y="62" width="833" height="1072" stroke-width="6"/>
        <rect x="100" y="82" width="793" height="1032" stroke-width="2"/>
        <line x1="110" y1="330" x2="496" y2="80" stroke-width="1.5"/>
        <line x1="883" y1="330" x2="496" y2="80" stroke-width="1.5"/>
        <line x1="0" y1="1180" x2="330" y2="880" stroke-width="1.5"/>
        <line x1="993" y1="1180" x2="663" y2="880" stroke-width="1.5"/>
        <line x1="0" y1="910" x2="110" y2="830" stroke-width="1.5"/>
        <line x1="993" y1="910" x2="883" y2="830" stroke-width="1.5"/>
        <polyline points="20,1070 140,1070 140,1180" stroke-width="1.5"/>
        <polyline points="973,1070 853,1070 853,1180" stroke-width="1.5"/>
        <polyline points="30,130 130,130 130,20" stroke-width="1.5"/>
        <polyline points="963,130 863,130 863,20" stroke-width="1.5"/>
      </g>
      <g fill="#e9b233">
        <circle cx="30" cy="30" r="9"/>
        <circle cx="963" cy="30" r="9"/>
        <circle cx="30" cy="1170" r="9"/>
        <circle cx="963" cy="1170" r="9"/>
        <circle cx="40" cy="1140" r="4"/>
        <circle cx="953" cy="1140" r="4"/>
        <circle cx="60" cy="1160" r="4"/>
        <circle cx="933" cy="1160" r="4"/>
      </g>
    </svg>

    <section class="content">
      <h2 class="event-host">Amber Staffing Pelovin</h2>
      <h1 class="event-title">Casino</h1>
      <p class="event-script">Night</p>
      <p class="event-date">THURSDAY, 7 NOVEMBER 2019</p>
      <div class="divider"></div>
      <p class="venue">Venue : Velvet Lantern Tavern Johannesburg<br>Orwin Tembe Plaza, 14 Corvell Lane, Sandton<br>Arrive : 18: 30</p>
      <div class="divider"></div>
      <p class="extras">Dress code: Smart Casual / Cocktail<br>Drinks &amp; Snacks will be provided<br>Entertainment : @dj_marlowtune</p>
      <p class="invite-line">You've earned your CA – now come play your winning hand!</p>
      <p class="rsvp">RSVP ASAP : Pelovin Representative</p>
    </section>
  </main>
</body>
</html>
```